Wendlake Business Cards

Front and back. Martin Colfax MBA is the CEO of Wendlake Homes. Black white and grays. Logo and cool design.

Target Market(s)

Professional lenders and investors

Industry/Entity Type

Real estate developer. NO HOUSES OR ROOFS

Contact Information for Business Card

Logo, name and unique design. Front and back. Martin Colfax MBA is the CEO of Wendlake Homes. Black white and grays. Logo and cool design.

Font styles to use
Sans Serif

Colors

Designer to choose only greyscale colors for use in the design.

Requirements
Must have
• Cool look. Not the same card I could design.
Nice to have
• Something memorable
Should not have
• Basic

```html
<!DOCTYPE html>
<html lang="en">
<head>
<meta charset="utf-8">
<title>Wendlake Business Cards</title>
<link href="https://fonts.googleapis.com/css2?family=Montserrat:ital,wght@0,400;0,700;1,700&display=swap" rel="stylesheet">
<style>
  :root {
    --backdrop: #e4e4e2;
    --ink: #0a0a0a;
    --paper: #ffffff;
    --line-gray: #8a8a8a;
    --soft-gray: #ececec;
  }
  * { margin: 0; padding: 0; box-sizing: border-box; }
  html, body {
    width: 1200px; height: 846px; overflow: hidden;
    background: var(--backdrop);
    font-family: "Montserrat", Arial, sans-serif;
    color: var(--ink);
  }
  .card {
    position: absolute; left: 346px; width: 508px; height: 290px; overflow: hidden;
  }
  .card--front { top: 99px; background: var(--paper); }
  .card--back { top: 456px; background: var(--ink); }

  .front-art {
    position: absolute; right: 0; top: 0; width: 200px; height: 290px;
    background: linear-gradient(135deg, rgba(255,255,255,0) 30%, var(--soft-gray) 60%, #dcdcdc 100%);
    clip-path: polygon(0 0, 100% 0, 100% 100%, 0 100%, 40% 60%);
  }

  .brand-vertical {
    position: absolute; left: 47px; top: 230px;
    transform: rotate(-90deg); transform-origin: left top;
    width: 162px; height: 50px;
    display: flex; flex-direction: column; align-items: center;
    font-weight: 700; line-height: 1;
  }
  .brand-vertical .brand-name { font-size: 29px; letter-spacing: -0.5px; }
  .brand-vertical .brand-sub { font-size: 8px; letter-spacing: 5px; margin-top: 5px; }

  .divider {
    position: absolute; left: 115px; top: 68px; width: 1px; height: 162px; background: var(--ink);
  }

  .person { position: absolute; left: 134px; top: 63px; }
  .person-name { font-size: 21px; font-weight: 700; line-height: 1.2; }
  .person-title { font-size: 17px; font-weight: 700; font-style: italic; line-height: 1.2; margin-top: 2px; }

  .contacts { position: absolute; left: 134px; top: 137px; list-style: none; }
  .contact {
    display: flex; align-items: center; height: 24.3px;
    font-size: 14.5px; font-weight: 400;
  }
  .contact svg { width: 16px; height: 16px; margin-right: 8px; flex: none; }

  .brand-lockup {
    position: absolute; left: 0; right: 0; top: 96px;
    display: flex; flex-direction: column; align-items: center;
    color: var(--paper); font-weight: 700; line-height: 1;
  }
  .brand-lockup .brand-name { font-size: 62px; letter-spacing: -1.5px; }
  .brand-lockup .brand-sub { font-size: 15px; letter-spacing: 12px; margin-top: 10px; }
</style>
</head>
<body>
  <section class="card card--front">
    <div class="front-art" role="img" aria-label="Architectural line drawing of angled building facades"></div>

    <div class="brand-vertical">
      <span class="brand-name">Wendlake</span>
      <span class="brand-sub">HOMES</span>
    </div>
    <div class="divider"></div>

    <div class="person">
      <p class="person-name">Martin Colfax</p>
      <p class="person-title">MBA CEO</p>
    </div>

    <ul class="contacts">
      <li class="contact">
        <svg viewBox="0 0 16 16" aria-hidden="true"><path d="M5 1h3v4H6.5v6H8v4H5c-1 0-2-2-2-7s1-7 2-7z" fill="#0a0a0a"/></svg>
        1-555-204-7310
      </li>
      <li class="contact">
        <svg viewBox="0 0 16 16" aria-hidden="true"><rect x="1" y="4" width="14" height="9" fill="#0a0a0a"/><path d="M1.5 4.5 8 9.5l6.5-5M1.5 12.5l5-4.5M14.5 12.5l-5-4.5" stroke="#fff" stroke-width="1" fill="none"/></svg>
        martin@wendlakehomes.com
      </li>
      <li class="contact">
        <svg viewBox="0 0 16 16" aria-hidden="true"><circle cx="8" cy="8" r="6" fill="#0a0a0a"/></svg>
        social.wendlakehomes.com
      </li>
      <li class="contact">
        <svg viewBox="0 0 16 16" aria-hidden="true"><circle cx="8" cy="8" r="7" fill="#0a0a0a"/><g stroke="#fff" stroke-width="0.9" fill="none"><ellipse cx="8" cy="8" rx="3" ry="7"/><path d="M1 8h14M2.5 4.5h11M2.5 11.5h11M8 1v14"/></g></svg>
        www.wendlakehomes.com
      </li>
    </ul>
  </section>

  <section class="card card--back">
    <div class="brand-lockup">
      <span class="brand-name">Wendlake</span>
      <span class="brand-sub">HOMES</span>
    </div>
  </section>
</body>
</html>
```